Solar appointment reminder card

We are looking for a new design for our appointment reminder card since we have changed our logo. The card should have the new logo along with space for the employee to hand write the customers appointment date, time, the employees name and phone number.
I've uploaded what our old basic appointment card looked like and our new logo.

The cards should be in a standard business card size and could be horizontal or vertical.

```html
<!DOCTYPE html>
<html lang="en">
<head>
<meta charset="utf-8">
<title>Orvalux Solar – Appointment Card</title>
<link href="https://fonts.googleapis.com/css2?family=Montserrat:wght@300;400;800&display=swap" rel="stylesheet">
<style>
  :root {
    --backdrop: #e6e7e9;
    --orange: #f5921f;
    --orange-text: #f08a1e;
    --sun-yellow: #fdc52a;
    --white: #ffffff;
    --shadow: rgba(0, 0, 0, 0.28);
  }
  * { margin: 0; padding: 0; box-sizing: border-box; }
  html, body {
    width: 1200px;
    height: 900px;
    overflow: hidden;
    background: var(--backdrop);
    font-family: "Montserrat", sans-serif;
  }
  .card {
    position: absolute;
    left: 285px;
    width: 628px;
    height: 359px;
    border-radius: 6px;
    overflow: hidden;
    box-shadow: 3px 4px 6px var(--shadow);
  }
  .card-front { top: 78px; background: var(--orange); }
  .card-back { top: 458px; background: var(--white); }

  /* Front */
  .brand-lockup {
    position: absolute;
    left: 0;
    right: 0;
    top: 112px;
    display: flex;
    align-items: center;
    justify-content: center;
    gap: 16px;
  }
  .brand-dot {
    width: 70px;
    height: 70px;
    border-radius: 50%;
    background: var(--sun-yellow);
    flex-shrink: 0;
  }
  .brand-text { display: flex; flex-direction: column; }
  .brand-name {
    color: var(--sun-yellow);
    font-weight: 800;
    font-size: 60px;
    line-height: 1;
    letter-spacing: -1px;
  }
  .brand-tagline {
    color: var(--sun-yellow);
    font-weight: 400;
    font-size: 16px;
    letter-spacing: 3.6px;
    margin-top: 8px;
  }
  .front-rule {
    position: absolute;
    left: 0;
    right: 0;
    top: 306px;
    height: 3px;
    background: var(--sun-yellow);
  }

  /* Back */
  .brand-lockup-small {
    position: absolute;
    left: 20px;
    top: 26px;
    display: flex;
    align-items: center;
    gap: 6px;
  }
  .brand-dot-small {
    width: 20px;
    height: 20px;
    border-radius: 50%;
    background: var(--sun-yellow);
  }
  .brand-name-small {
    color: var(--orange-text);
    font-weight: 800;
    font-size: 17px;
    line-height: 1;
  }
  .rule {
    position: absolute;
    left: 0;
    right: 0;
    height: 3px;
    background: var(--sun-yellow);
  }
  .divider {
    position: absolute;
    left: 229px;
    top: 123px;
    bottom: 2px;
    width: 3px;
    background: var(--sun-yellow);
  }
  .heading {
    position: absolute;
    left: 0;
    right: 0;
    top: 86px;
    height: 37px;
    display: flex;
    align-items: center;
    justify-content: center;
    color: var(--orange-text);
    font-weight: 300;
    font-size: 16px;
    letter-spacing: 6px;
  }
  .field-label {
    position: absolute;
    left: 0;
    width: 229px;
    display: flex;
    align-items: center;
    justify-content: center;
    color: var(--orange-text);
    font-weight: 300;
    font-size: 12px;
    letter-spacing: 5px;
  }
</style>
</head>
<body>
  <section class="card card-front">
    <div class="brand-lockup">
      <span class="brand-dot"></span>
      <div class="brand-text">
        <span class="brand-name">ORVALUX</span>
        <span class="brand-tagline">ORVALUX SOLAR CO</span>
      </div>
    </div>
    <div class="front-rule"></div>
  </section>

  <section class="card card-back">
    <div class="brand-lockup-small">
      <span class="brand-dot-small"></span>
      <span class="brand-name-small">ORVALUX</span>
    </div>

    <div class="rule" style="top:83px"></div>
    <h1 class="heading">APPOINTMENT</h1>
    <div class="rule" style="top:122px"></div>

    <div class="field-label" style="top:125px;height:57px">DATE</div>
    <div class="rule" style="top:182px"></div>
    <div class="field-label" style="top:185px;height:57px">TIME</div>
    <div class="rule" style="top:242px"></div>
    <div class="field-label" style="top:245px;height:58px">REPRESENTATIVE</div>
    <div class="rule" style="top:303px"></div>
    <div class="field-label" style="top:306px;height:53px">PHONE</div>

    <div class="divider"></div>
  </section>
</body>
</html>
```